qoVantix Employee-Centric Engagement brochure

Design a 2-page 81/2" x 11'' brochure (front and back) that includes our logo and some pictures. We need it in a format that we can print from and edit. Word or PDF would be good. We need to be able to give the file to a printing company or ShipLark office for them to print for us. We conduct frequent employee surveys as well as providing coaching to employees and managers around the data. Our goal is to get employees engaged in continuous improvement and in making their teams and workplace the best it can be. We have been in business for 20 years and this is an extension of what we have been doing in the past. Bringing the ownership of engagement and improvement to the employees rather than having managers responsible for employee engagement and process improvement. Our Energy metric is research based and predicts performance. Our web site is www.qovantix.example. I've attached a Word document with our first pass at content. Please improve greatly on this.

Target Market(s)

Company managers and senior HR personnel

Industry/Entity Type

Employee

Font styles to use
Sans Serif

Colors

Designer to choose colors to be used in the design.

Requirements
Must have
• All of the information in the documents sent and some appropriate pictures/background

```html
<!DOCTYPE html>
<html lang="en">
<head>
<meta charset="utf-8">
<title>qoVantix Employee-Centric Engagement Brochure</title>
<link rel="stylesheet" href="https://fonts.googleapis.com/css2?family=Montserrat:ital,wght@0,500;0,600;0,700;1,800&family=Oswald:wght@300;400&family=Roboto+Condensed:wght@300;400&display=swap">
<style>
:root{
  --orange:#e8702a;
  --navy:#1f2d3a;
  --cyan:#29b6e8;
  --grey:#6d6e71;
  --light-grey:#8a8b8e;
  --green:#2e8b3a;
  --maroon:#a3173a;
  --ink:#222;
  --white:#fff;
}
*{box-sizing:border-box;margin:0;padding:0}
html,body{width:1200px;height:781px;overflow:hidden;background:var(--white)}
body{position:relative;font-family:"Roboto Condensed",Arial,sans-serif}
.page{position:absolute;top:38px;width:543px;height:702px;background:var(--white);overflow:hidden;box-shadow:0 4px 10px rgba(0,0,0,.35)}
.page--front{left:32px}
.page--back{left:623px}

/* shared */
.brand{display:flex;align-items:center}
.brand__name{font-family:"Montserrat",sans-serif;font-weight:600;color:var(--white);font-size:24px;letter-spacing:.2px}
.footer-band{position:absolute;left:0;bottom:0;width:100%;height:32px;background:var(--navy)}
.footer-band .brand{position:absolute;right:12px;top:0;height:32px}
.footer-band .brand__name{font-size:18px}

/* front */
.hero-photo{position:absolute;left:0;top:0;width:100%;height:250px;
  background:linear-gradient(100deg,#2b3a52 0%,#56678a 35%,#c9ccd2 60%,#e5e2dc 80%,#b9bcc4 100%)}
.page--front .hero-brand{position:absolute;left:32px;top:178px}
.headline{position:absolute;left:32px;top:256px;font-family:"Montserrat",sans-serif;font-weight:800;font-style:italic;color:var(--orange);font-size:31px;line-height:33px;letter-spacing:.3px}
.list-block{position:absolute;left:32px;width:290px}
.list-block--moving{top:336px}
.list-block--simple{top:469px}
.list-title{font-family:"Montserrat",sans-serif;font-weight:600;font-style:italic;color:var(--grey);font-size:13px;margin-bottom:2px}
.bullets{list-style:none;font-weight:300;color:var(--grey);font-size:10px}
.bullets li{position:relative;padding-left:16px;line-height:20px}
.bullets li::before{content:"";position:absolute;left:6px;top:9px;width:3px;height:3px;border-radius:50%;background:var(--grey)}
.roles-box{position:absolute;left:314px;top:340px;width:218px;height:112px;background:var(--navy);
  clip-path:polygon(8% 0,100% 0,100% 100%,0 100%);color:var(--white);font-family:"Montserrat",sans-serif;text-align:right;padding:18px 20px 0 0}
.roles-box .small{font-weight:600;font-size:12px;letter-spacing:1.4px;line-height:14px}
.roles-box .large{font-weight:700;font-size:17.5px;letter-spacing:.8px;line-height:20px;margin-bottom:6px}
.roles-box .small2{font-weight:500;font-size:11.5px;letter-spacing:.9px}
.quote-box{position:absolute;left:284px;top:462px;width:248px;height:112px;background:var(--orange);
  clip-path:polygon(12% 0,100% 0,100% 100%,0 100%);color:var(--white);font-family:"Oswald",sans-serif;font-weight:300;font-size:24px;line-height:32px;text-align:right;padding:8px 20px 0 0}
.intro{position:absolute;left:32px;top:584px;width:476px;font-weight:300;color:var(--light-grey);font-size:10px;line-height:20px}

/* back */
.team-photo{position:absolute;left:0;top:0;width:100%;height:235px;
  background:radial-gradient(circle at 70% 20%,#f1b06a 0%,#c0773e 25%,transparent 55%),linear-gradient(180deg,#8a5d3c 0%,#3d3a3a 60%,#1e2228 100%)}
.roles-statement{position:absolute;left:32px;top:152px;font-family:"Oswald",sans-serif;font-weight:300;color:var(--white);font-size:19.5px;line-height:25.5px}
.process{position:absolute;left:10px;top:247px;width:521px;height:383px}
.enhance{position:absolute;left:385px;top:376px;font-family:"Oswald",sans-serif;font-weight:300;color:var(--ink);font-size:15px;line-height:25px;letter-spacing:.3px}
.call{position:absolute;left:32px;top:640px;font-family:"Oswald",sans-serif;font-weight:300;color:var(--ink);font-size:19px}
.site-url{position:absolute;left:32px;top:9px;color:#c8cdd3;font-size:9.5px;letter-spacing:2px}
.hex-text{font-family:"Montserrat",sans-serif;font-weight:600;font-size:10.5px;text-anchor:middle}
.process-title{font-family:"Oswald",sans-serif;font-weight:300;font-size:14px;fill:var(--ink)}
</style>
</head>
<body>

<section class="page page--front">
  <div class="hero-photo" role="img" aria-label="Photo: smiling businessman raising a fist in celebration with colleagues in an office"></div>
  <div class="brand hero-brand"><span class="brand__name">qoVantix</span></div>

  <h1 class="headline">FOCUS EMPLOYEE ENERGY<br>ON WHAT REALLY MATTERS</h1>

  <div class="list-block list-block--moving">
    <h2 class="list-title">BY MOVING UP TO</h2>
    <ul class="bullets">
      <li>Empowering employees to own their own engagement and energy</li>
      <li>Managers are teachers and advisors vs. survey interpreters</li>
      <li>On-going and frequent process built the way you do business</li>
      <li>Backed by the science of human energy at work</li>
      <li>Documented return on investment (ROI)</li>
    </ul>
  </div>

  <div class="list-block list-block--simple">
    <h2 class="list-title">SIMPLE FAST PROVEN</h2>
    <ul class="bullets">
      <li>Transforming employee engagement with a proven model</li>
      <li>Simple and fast implementation</li>
      <li>Quick and easy process for users</li>
      <li>Celebrations focused on documented results</li>
    </ul>
  </div>

  <div class="roles-box">
    <p class="small">CHANGING THE ROLES</p>
    <p class="large">OF ENGAGEMENT</p>
    <p class="small2">CHANGING THE ATTITUDES</p>
    <p class="large">OF ENGAGEMENT</p>
  </div>

  <div class="quote-box">“IT WORKS;<br>NOT A SURVEY;<br>LEARNING FOR ALL”</div>

  <p class="intro">Employee-centric engagement uses a new lens to bring people together to drive positive change. Through a data-driven process, frequent pulsing is focused on the employee learning from their own data. Employees learn and reflect and then engage with peer ambassadors who use root-cause analysis, ideation and other tools to focus learning and present 3 improvement ideas to managers. Return on investment projections are done for each idea.</p>

  <footer class="footer-band">
    <div class="brand"><span class="brand__name">qoVantix</span></div>
  </footer>
</section>

<section class="page page--back">
  <div class="team-photo" role="img" aria-label="Photo: team members stacking their hands together in warm sunlight"></div>
  <p class="roles-statement">MANAGERS DELEGATE, COACH AND TEACH.<br>AMBASSADORS ARE FACILITATORS AND CO-CREATORS.<br>EMPLOYEES ARE AGENTS OF CHANGE AND IMPROVEMENT.</p>

  <svg class="process" viewBox="0 0 651 478" aria-label="Employee-centric engagement process cycle">
    <defs>
      <marker id="head-blue" viewBox="0 0 10 10" refX="5" refY="5" markerWidth="3" markerHeight="3" orient="auto"><path d="M0 0L10 5L0 10z" fill="var(--cyan)"/></marker>
      <marker id="head-orange" viewBox="0 0 10 10" refX="5" refY="5" markerWidth="3" markerHeight="3" orient="auto"><path d="M0 0L10 5L0 10z" fill="var(--orange)"/></marker>
      <marker id="head-green" viewBox="0 0 10 10" refX="5" refY="5" markerWidth="3" markerHeight="3" orient="auto"><path d="M0 0L10 5L0 10z" fill="var(--green)"/></marker>
      <marker id="head-maroon" viewBox="0 0 10 10" refX="5" refY="5" markerWidth="3" markerHeight="3" orient="auto"><path d="M0 0L10 5L0 10z" fill="var(--maroon)"/></marker>
      <marker id="head-navy" viewBox="0 0 10 10" refX="5" refY="5" markerWidth="3" markerHeight="3" orient="auto"><path d="M0 0L10 5L0 10z" fill="var(--navy)"/></marker>
    </defs>
    <g fill="var(--navy)">
      <polygon points="0,0 88,0 0,138"/>
      <polygon points="0,340 88,478 0,478"/>
      <polygon points="393,0 651,0 651,138 456,138"/>
      <polygon points="458,338 651,338 651,478 393,478"/>
    </g>
    <text class="process-title" x="106" y="21">EMPLOYEE-CENTRIC ENGAGEMENT PROCESS</text>

    <g fill="var(--white)" stroke-width="1.3">
      <polygon points="157,108 194,43 270,43 307,108 270,173 194,173" stroke="var(--orange)"/>
      <polygon points="266,215 303,150 379,150 416,215 379,280 303,280" stroke="var(--green)"/>
      <polygon points="246,360 283,295 359,295 396,360 359,425 283,425" stroke="var(--maroon)"/>
      <polygon points="68,360 105,295 181,295 218,360 181,425 105,425" stroke="var(--navy)"/>
      <polygon points="49,215 86,150 162,150 199,215 162,280 86,280" stroke="var(--cyan)"/>
    </g>

    <g class="hex-text" fill="var(--orange)">
      <text x="232" y="84">FREQUENT</text><text x="232" y="98">PULSING (3 TO 5</text><text x="232" y="112">QUESTIONS TO</text><text x="232" y="126">SPARK</text><text x="232" y="140">LEARNING)</text>
    </g>
    <g class="hex-text" fill="var(--green)">
      <text x="341" y="199">EMPLOYEES</text><text x="341" y="213">REVIEW TREND</text><text x="341" y="227">DATA AND</text><text x="341" y="241">JOURNAL</text>
    </g>
    <g class="hex-text" fill="var(--maroon)">
      <text x="321" y="347">AMBASSADORS</text><text x="321" y="361">GUIDE</text><text x="321" y="375">IMPROVEMENT</text><text x="321" y="389">DIALOGUE</text>
    </g>
    <g class="hex-text" fill="var(--navy)">
      <text x="143" y="351">3 IDEAS</text><text x="143" y="365">PRESENTED TO</text><text x="143" y="379">MANAGER</text>
    </g>
    <g class="hex-text" fill="var(--cyan)">
      <text x="124" y="205">MANAGER HELPS</text><text x="124" y="219">FACILITATE</text><text x="124" y="233">IMPLEMENTATION</text>
    </g>

    <g fill="none" stroke-width="9">
      <path d="M118 130 Q126 88 150 80" stroke="var(--cyan)" marker-end="url(#head-blue)"/>
      <path d="M314 72 Q350 90 360 120" stroke="var(--orange)" marker-end="url(#head-orange)"/>
      <path d="M420 245 Q420 290 395 305" stroke="var(--green)" marker-end="url(#head-green)"/>
      <path d="M275 436 Q250 455 208 440" stroke="var(--maroon)" marker-end="url(#head-maroon)"/>
      <path d="M70 325 Q40 300 45 260" stroke="var(--navy)" marker-end="url(#head-navy)"/>
    </g>
  </svg>

  <p class="enhance">ENHANCE FIRM<br>PERFORMANCE BY<br>CHANGING HOW YOUR<br>BUSINESS LISTENS<br>AND LEARNS</p>

  <p class="call">Call today: +1 555-014-2290, or write to info@qovantix.example</p>

  <footer class="footer-band">
    <span class="site-url">www.qovantix.example</span>
    <div class="brand"><span class="brand__name">qoVantix</span></div>
  </footer>
</section>

</body>
</html>
```